Webdesign für Online-Shop für Honig
Zielgruppe
Verkauf von Sidr Honig. Ein sehr hochwertiger Premium-Honig aus dem Jemen.
Aufgabenstellung
Zu Erstellen ist ein Design für einen Onlineshop. Der Onlineshop verkauft Kosmetik-, Lebensmittel- und Gesundheitsprodukte die alle auf einem Honig basieren.
Domain: qalvenu.com
Die Seite soll sehr hochwertig und orientalisch wirken. Der Hintergrund soll auf jeden Fall dunkel sein.
Wir benötigen ein Screendesign der:
- Home-Seite,
- Über uns-Seite
- Produktdetailseite.
Die Designs müssen nicht per HTML umgesetzt werden, können aber. Es reicht ein reines Design als Bild, HTML ist aber auch in Ordnung.
Bitte hochwertige Stockbilder nutzen.

```html
<!DOCTYPE html>
<html lang="en">
<head>
<meta charset="utf-8">
<title>Qalvenu – Menu</title>
<link rel="stylesheet" href="https://fonts.googleapis.com/css2?family=Cormorant+Garamond:wght@400&display=swap">
<style>
  :root {
    --bg: #000000;
    --gold: #d3955f;
    --ornament: #2e2216;
    --ornament-soft: #1a130c;
  }
  * { margin: 0; padding: 0; box-sizing: border-box; }
  html, body { width: 1200px; height: 832px; overflow: hidden; background: var(--bg); }
  .menu-screen {
    position: relative;
    width: 1200px;
    height: 832px;
    overflow: hidden;
    background: var(--bg);
    font-family: "Cormorant Garamond", Georgia, serif;
    color: var(--gold);
  }
  .ornament {
    position: absolute;
    top: 89px;
    width: 686px;
    height: 686px;
    border-radius: 50%;
    background: radial-gradient(circle, var(--ornament) 0%, var(--ornament-soft) 70%, rgba(0,0,0,0) 100%);
  }
  .ornament--left { left: -350px; }
  .ornament--right { left: 862px; }
  .brand {
    position: absolute;
    left: 100px;
    top: 68px;
    display: flex;
    align-items: center;
    gap: 40px;
    height: 57px;
  }
  .brand-mark {
    width: 54px;
    height: 54px;
    border: 1.5px solid var(--gold);
    border-radius: 50%;
  }
  .brand-name {
    font-size: 26px;
    letter-spacing: 1px;
    color: var(--gold);
  }
  .close-button {
    position: absolute;
    left: 1042px;
    top: 66px;
    width: 41px;
    height: 41px;
  }
  .main-nav {
    position: absolute;
    left: 0;
    top: 206px;
    width: 1200px;
    list-style: none;
    text-align: center;
  }
  .main-nav li {
    height: 91px;
    line-height: 91px;
    font-size: 68px;
    position: relative;
  }
  .main-nav a { color: var(--gold); text-decoration: none; }
  .nav-item--active::before,
  .nav-item--active::after {
    content: "";
    position: absolute;
    top: 50%;
    width: 72px;
    border-top: 2px dotted var(--gold);
  }
  .nav-item--active::before { left: 416px; }
  .nav-item--active::after { left: 710px; }
</style>
</head>
<body>
<div class="menu-screen">
  <div class="ornament ornament--left" role="img" aria-label="Ornate oriental mandala pattern in dark bronze"></div>
  <div class="ornament ornament--right" role="img" aria-label="Ornate oriental mandala pattern in dark bronze"></div>

  <header class="brand">
    <span class="brand-mark"></span>
    <span class="brand-name">qalvenu</span>
  </header>

  <svg class="close-button" viewBox="0 0 41 41" aria-label="Close menu">
    <line x1="1" y1="1" x2="40" y2="40" stroke="#d3955f" stroke-width="2.5"/>
    <line x1="40" y1="1" x2="1" y2="40" stroke="#d3955f" stroke-width="2.5"/>
  </svg>

  <ul class="main-nav">
    <li><a href="#">About Us</a></li>
    <li><a href="#">History</a></li>
    <li><a href="#">Healthy</a></li>
    <li class="nav-item--active"><a href="#">Beauty</a></li>
    <li><a href="#">Tasty</a></li>
  </ul>
</div>
</body>
</html>
```